Product Marketing Slick / Product Brief. 1 sheet now then an additional 2 plus more in the future.

We need to create 1 page product sheets that will be used for marketing purposes.
The products we are selling are network security and network compliance for PCI, HIPAA and GDPR.
We will essentially be doing all of the consulting to make their networks secure, then on a daily basis be scanning and validating that all of the government requirements are being met for compliance.
We dont want to make this too technical so its more of a page that will discuss in general terms what we do and why its important for them to have our services.
***Note There will be a total of Three Sheets, this project is for the first one and can be for any one of the products. HIPAA Compliance , PCI Compliance or GDPR Compliance.
We will contract with you to do the additional 2 pages and probably more if we select your design.
Target Market(s)
Medical, Hospitality
Industry/Entity Type
Medical
Colors
Designer to choose colors to be used in the design.
Look and feel

```html
<!DOCTYPE html>
<html lang="en">
<head>
<meta charset="utf-8">
<title>Verant – HIPAA Compliance Product Sheet</title>
<link href="https://fonts.googleapis.com/css2?family=Lato:ital,wght@0,400;0,700;0,900;1,700&display=swap" rel="stylesheet">
<style>
  :root{
    --stage:#d6d6d6;
    --paper:#ffffff;
    --brand-blue:#1a8ad4;
    --deep-blue:#0c5e9c;
    --brand-green:#8cc63f;
    --dark-green:#5aa02c;
    --ink:#333a40;
    --muted:#5b646b;
  }
  *{box-sizing:border-box;margin:0;padding:0}
  html,body{width:778px;height:1200px;overflow:hidden}
  body{background:var(--stage);font-family:"Lato",Arial,sans-serif;color:var(--ink);position:relative}
  .sheet{position:absolute;left:19px;top:77px;width:740px;height:1046px;background:var(--paper);overflow:hidden;box-shadow:0 2px 6px rgba(0,0,0,.15)}
  .header-art{position:absolute;left:0;top:0;width:740px;height:430px}
  .brand{position:absolute;display:flex;align-items:center;gap:8px}
  .brand-dot{width:18px;height:18px;border-radius:50%;background:var(--brand-green)}
  .brand-name{font-weight:900;letter-spacing:3px;color:var(--paper);font-size:22px}
  .brand--top{left:28px;top:22px}
  .brand--foot{left:420px;top:862px}
  .brand--foot .brand-name{color:var(--brand-blue);font-size:30px}
  .brand--foot .brand-dot{width:26px;height:26px}
  .pillars{position:absolute;top:440px;left:0;width:740px;text-align:center;font-weight:900;font-size:33px;color:var(--brand-blue);letter-spacing:2px}
  .pillars .sep{color:var(--brand-green);margin:0 14px}
  .rule{position:absolute;top:492px;left:36px;width:668px;height:2px;background:var(--brand-green)}
  .tagline{position:absolute;top:506px;left:36px;font-style:italic;font-weight:700;font-size:27px;color:var(--brand-green)}
  .body-copy{position:absolute;top:556px;left:36px;width:668px}
  .body-copy h2{font-size:16px;font-weight:900;color:var(--ink);line-height:1.35}
  .body-copy h3{font-size:14px;font-weight:700;color:var(--ink);margin-bottom:10px}
  .body-copy p{font-size:12.5px;line-height:1.55;color:var(--muted);margin-bottom:8px}
  .contact{position:absolute;left:0;top:800px;width:270px;height:246px;background:var(--brand-blue);color:var(--paper);padding:28px 30px;font-size:12.5px;line-height:1.7}
  .contact h4{font-size:15px;font-weight:900;margin-bottom:6px}
  .foot-art{position:absolute;left:270px;top:800px;width:470px;height:246px}
</style>
</head>
<body>
  <main class="sheet">
    <svg class="header-art" viewBox="0 0 740 430" aria-hidden="false">
      <defs>
        <linearGradient id="photoTone" x1="0" y1="0" x2="1" y2="1">
          <stop offset="0" stop-color="#0d3f6e"/>
          <stop offset=".5" stop-color="#2a78b8"/>
          <stop offset="1" stop-color="#8fbfe2"/>
        </linearGradient>
      </defs>
      <rect width="740" height="430" fill="#ffffff"/>
      <path d="M0 0 H740 V20 C520 10 260 30 0 90 Z" fill="var(--deep-blue)"/>
      <path d="M0 90 C260 30 520 10 740 20 V40 C520 34 280 54 0 112 Z" fill="var(--brand-green)"/>
      <path d="M0 112 C280 54 520 34 740 40 V410 H0 Z" fill="url(#photoTone)" role="img" aria-label="Photo of a businessman in a suit reaching toward a glowing digital network display"/>
      <path d="M0 390 C240 420 520 380 740 398 V410 C520 392 240 432 0 402 Z" fill="var(--brand-green)"/>
    </svg>
    <div class="brand brand--top"><span class="brand-dot"></span><span class="brand-name">VERANT</span></div>

    <div class="pillars">SMART<span class="sep">•</span>SIMPLE<span class="sep">•</span>SAFE<span class="sep">•</span>SECURE</div>
    <div class="rule"></div>
    <p class="tagline">We worry, so you don't have to.</p>

    <section class="body-copy">
      <h2>Health Insurance Portability &amp; Accountability Act. (HIPAA)</h2>
      <h3>HIPAA (Health Insurance Portability &amp; Accountability Act.)</h3>
      <p>Digital health records have made patient care faster, but they have also made patient data a target. Under HIPAA, every practice that stores or shares protected health information must guard it with clear safeguards, regular checks and documented policies. We design a secure network around your practice, then scan and validate it every day so gaps are found and fixed before they become fines or breaches. Our team handles the technical work and the paperwork, keeping you ready for any audit.</p>
      <p>Do you really want to learn all the complexities of HIPAA and PCI compliance? No? Then leave it to us.</p>
      <p>We'll handle everything from start to finish and keep your business compliant so you never have to think about it again.</p>
    </section>

    <aside class="contact">
      <h4>Contact Us</h4>
      <p>Verant Inc.<br>2450 Harbor Lane, Suite 300<br>Brookfield, OR 97012<br>Phone: 555-014-7720<br>E-mail: info@verantsecure.com</p>
    </aside>

    <svg class="foot-art" viewBox="0 0 470 246" aria-hidden="true">
      <path d="M0 0 H470 V6 H0 Z" fill="var(--brand-blue)"/>
      <path d="M120 246 C260 200 380 180 470 130 V150 C380 196 280 220 170 246 Z" fill="var(--brand-green)"/>
      <path d="M230 246 C330 220 410 200 470 170 V246 Z" fill="var(--dark-green)"/>
    </svg>
    <div class="brand brand--foot"><span class="brand-dot"></span><span class="brand-name">VERANT</span></div>
  </main>
</body>
</html>
```